Stationery Design For Specialist London law firm

We have merged two firms of London lawyers to create a new firm with a new name.

The new firms name is RK Dunmore. We would like to include the description Solicitors and Advocates in the design.

We need a new design for our headed paper, business cards compliment slips etc.

The image we wish to project is fresh but not gimmicky - reliable and strong but not stuffy.

We have no strong views on font or colour this really is pretty much a blank page.

Our preference is for the name to be at the top of the page

Target Market(s)

Our clients who are individuals rather than corporate and other lawyers

Industry/Entity Type

Law Firm

Requirements
Should not have
• Legal images eg scales of justice etc

Obviously nothing childish or gimmicky

```html
<!DOCTYPE html>
<html lang="en">
<head>
<meta charset="utf-8">
<title>RK Dunmore – Stationery</title>
<link rel="stylesheet" href="https://fonts.googleapis.com/css2?family=Michroma&display=swap">
<style>
  :root {
    --backdrop: #dcdcd9;
    --paper: #ffffff;
    --brand-blue: #1f4e94;
    --bright-blue: #1a63b0;
    --grey-text: #6a6a6a;
    --dark-text: #3a3a3a;
    --font-brand: "Michroma", sans-serif;
  }
  * { box-sizing: border-box; margin: 0; padding: 0; }
  html, body {
    width: 1200px; height: 849px; overflow: hidden;
    background: var(--backdrop);
    font-family: var(--font-brand);
  }
  .canvas { position: relative; width: 1200px; height: 849px; }

  .sheet { position: absolute; background: var(--paper); box-shadow: 0 1px 3px rgba(0,0,0,.15); }

  /* Name line: square, name, divider, descriptor — all on one row */
  .brand { display: flex; align-items: center; white-space: nowrap; line-height: 1; }
  .brand-square { flex: none; background: var(--brand-blue); }
  .firm-name { color: var(--brand-blue); }
  .brand-divider { flex: none; align-self: stretch; background: var(--grey-text); opacity: .5; }
  .descriptor { color: var(--grey-text); }

  .brand.size-lg .brand-square { width: 12px; height: 12px; margin-right: 9px; }
  .brand.size-lg .firm-name { font-size: 17px; }
  .brand.size-lg .brand-divider { width: 1px; margin: 0 12px; }
  .brand.size-lg .descriptor { font-size: 8px; }

  .brand.size-sm .brand-square { width: 7px; height: 7px; margin-right: 5px; }
  .brand.size-sm .firm-name { font-size: 10px; }
  .brand.size-sm .brand-divider { width: 1px; margin: 0 6px; }
  .brand.size-sm .descriptor { font-size: 4.6px; }

  .brand.on-blue .brand-square { background: #ffffff; }
  .brand.on-blue .firm-name { color: #ffffff; }
  .brand.on-blue .brand-divider { background: #ffffff; }
  .brand.on-blue .descriptor { color: #e6eefa; }

  .footer-line { position: absolute; left: 0; right: 0; text-align: center; text-transform: uppercase;
    color: var(--dark-text); font-size: 5.4px; letter-spacing: .1px; line-height: 2; white-space: nowrap; }
  .footer-line .label, .footer-line .web { color: var(--bright-blue); }
  .footer-line .sep { color: var(--grey-text); padding: 0 4px; }

  /* Letterhead */
  .letterhead { left: 46px; top: 40px; width: 594px; height: 768px; }
  .letterhead .brand { position: absolute; left: 0; right: 0; top: 82px; justify-content: center; }
  .letterhead .footer-line { top: 726px; }

  /* Business card front */
  .card-front { left: 562px; top: 152px; width: 244px; height: 140px; }
  .card-front .brand { position: absolute; left: 14px; top: 24px; }
  .card-front .contact { position: absolute; right: 112px; top: 76px; text-align: right;
    font-size: 4.2px; line-height: 1.6; color: var(--dark-text); text-transform: uppercase; white-space: nowrap; }
  .card-front .contact .label { color: var(--bright-blue); display: inline-block; width: 18px; text-align: right; }
  .card-front .contact .web { color: var(--bright-blue); }
  .card-front .person { position: absolute; left: 158px; top: 77px; text-transform: uppercase; }
  .card-front .person-name { font-size: 7px; color: var(--brand-blue); display: block; }
  .card-front .person-role { font-size: 4.6px; color: var(--dark-text); display: block; margin-top: 3px; }

  /* Business card back */
  .card-back { left: 838px; top: 152px; width: 242px; height: 140px;
    background: radial-gradient(ellipse at 50% 55%, #1a6cc0 0%, #1553a0 45%, #163f86 100%); }
  .card-back .brand { position: absolute; left: 0; right: 0; top: 64px; justify-content: center; }

  /* Envelope */
  .envelope { left: 490px; top: 322px; width: 665px; height: 408px; background: transparent; box-shadow: none; }
  .envelope-flap { position: absolute; left: 0; top: 0; width: 665px; height: 118px;
    border-radius: 16px 16px 0 0;
    background: radial-gradient(ellipse at 50% 40%, #1c5dae 0%, #1f4690 40%, #222f6c 100%); }
  .envelope-flap .brand { position: absolute; left: 0; right: 0; top: 52px; justify-content: center; transform: rotate(180deg); }
  .envelope-body { position: absolute; left: 0; top: 118px; width: 665px; height: 290px; background: var(--paper);
    box-shadow: 0 1px 3px rgba(0,0,0,.15); }
  .envelope-body .brand { position: absolute; left: 30px; top: 44px; }
  .envelope-body .footer-line { top: 254px; }
</style>
</head>
<body>
<main class="canvas">

  <section class="sheet letterhead" aria-label="Letterhead">
    <div class="brand size-lg">
      <span class="brand-square"></span>
      <span class="firm-name">RK Dunmore</span>
      <span class="brand-divider"></span>
      <span class="descriptor">Solicitors and Advocates</span>
    </div>
    <p class="footer-line">
      24 Carrick Lane, North West London, NW3 5QT<span class="sep">|</span><span class="label">Tel</span> 02074 382 519<span class="sep">|</span><span class="label">Fax</span> 02074 382 519<span class="sep">|</span><span class="label">Email</span> daniel.hart@rkdunmore.co.uk<br>
      <span class="web">www.rkdunmore.co.uk</span>
    </p>
  </section>

  <section class="sheet card-front" aria-label="Business card front">
    <div class="brand size-sm">
      <span class="brand-square"></span>
      <span class="firm-name">RK Dunmore</span>
      <span class="brand-divider"></span>
      <span class="descriptor">Solicitors and Advocates</span>
    </div>
    <p class="contact">
      24 Carrick Lane<br>
      North West London, NW3 5QT<br>
      02074 382 519 <span class="label">Tel</span><br>
      02074 382 519 <span class="label">Fax</span><br>
      daniel.hart@rkdunmore.co.uk <span class="label">Email</span><br>
      <span class="web">www.rkdunmore.co.uk</span>
    </p>
    <p class="person">
      <span class="person-name">Daniel Hart</span>
      <span class="person-role">Lawyer</span>
    </p>
  </section>

  <section class="sheet card-back" aria-label="Business card back">
    <div class="brand size-sm on-blue">
      <span class="brand-square"></span>
      <span class="firm-name">RK Dunmore</span>
      <span class="brand-divider"></span>
      <span class="descriptor">Solicitors and Advocates</span>
    </div>
  </section>

  <section class="sheet envelope" aria-label="Envelope">
    <div class="envelope-flap">
      <div class="brand size-sm on-blue">
        <span class="brand-square"></span>
        <span class="firm-name">RK Dunmore</span>
        <span class="brand-divider"></span>
        <span class="descriptor">Solicitors and Advocates</span>
      </div>
    </div>
    <div class="envelope-body">
      <div class="brand size-lg">
        <span class="brand-square"></span>
        <span class="firm-name">RK Dunmore</span>
        <span class="brand-divider"></span>
        <span class="descriptor">Solicitors and Advocates</span>
      </div>
      <p class="footer-line">
        24 Carrick Lane, North West London, NW3 5QT<span class="sep">|</span><span class="label">Tel</span> 02074 382 519<span class="sep">|</span><span class="label">Fax</span> 02074 382 519<span class="sep">|</span><span class="label">Email</span> daniel.hart@rkdunmore.co.uk<br>
        <span class="web">www.rkdunmore.co.uk</span>
      </p>
    </div>
  </section>

</main>
</body>
</html>
```